Regional Sales Company Needs Professional Document Design

We are an American Midwest company that needs clean, polished document layouts that effectively communicate the most critical information to the recipient. This project is specifically for a sales quote, but additional documents (subsequent work) need a consistent look. Our primary design guidelines are: 1) Use the same colors and logos provided. 2) minimize the amount of space the header occupies on the document. 3) Prioritize the information as it has been numbered in the attachment (1 - 5). 4) Redesign the footer logo/image. The information must stay the same, but present it as you see fit.

I have attached a draft and an annotation layout. The draft shows the overall structure and information on the document. The Annotation layout has the numbering referenced and some additional notes.

Industry/Entity Type

HVAC Supplier

Colors
0054AA
0677BA
7BADD7
CADEEF
E8F1F8

Requirements
Must have
• Maintain overall structure of draft. E.g. No left to right documents

```html
<!DOCTYPE html>
<html lang="en">
<head>
<meta charset="utf-8">
<title>Quotation Q000039 – Northline Climate Supply</title>
<link href="https://fonts.googleapis.com/css2?family=Source+Sans+3:wght@400;600;700&display=swap" rel="stylesheet">
<style>
  :root{
    --brand-blue:#0054AA;
    --mid-blue:#0677BA;
    --sky-blue:#7BADD7;
    --pale-blue:#CADEEF;
    --mist-blue:#E8F1F8;
    --white:#ffffff;
  }
  *{box-sizing:border-box;margin:0;padding:0}
  html,body{width:927px;height:1200px;overflow:hidden;background:var(--white)}
  body{font-family:"Source Sans 3",Arial,sans-serif;color:var(--brand-blue);position:relative}
  .document{position:relative;width:927px;height:1200px;overflow:hidden}

  /* Header */
  .header{position:absolute;left:0;top:0;width:927px;height:180px}
  .header-panel{position:absolute;left:340px;top:0;width:587px;height:165px;background:var(--mist-blue)}
  .corner-shapes{position:absolute;right:0;top:0}
  .brand{position:absolute;left:40px;top:52px;display:flex;align-items:center;gap:12px}
  .brand-dot{width:52px;height:52px;border-radius:50%;background:var(--brand-blue)}
  .brand-name{font-size:30px;font-weight:600;color:var(--brand-blue);line-height:1.05}
  .project{position:absolute;left:392px;top:50px}
  .label{font-weight:700;font-size:14px;letter-spacing:.2px}
  .project-address{font-size:14px;line-height:19px;margin-top:3px}
  .quote-number{position:absolute;left:392px;top:124px;font-size:17px;font-weight:700}
  .quote-number span{font-weight:400;font-size:15px;margin-left:6px}
  .doc-title{position:absolute;left:678px;top:136px;font-size:22px;font-weight:700;letter-spacing:8px;color:var(--brand-blue)}

  /* Terms */
  .terms{position:absolute;left:38px;top:195px;width:856px;font-size:10.3px;line-height:12.9px;color:var(--brand-blue)}
  .terms p{margin:0}

  /* Footer */
  .footer{position:absolute;left:0;top:1093px;width:927px;height:107px;background:var(--brand-blue);color:var(--white)}
  .footer-shapes{position:absolute;left:0;top:0}
  .tagline{position:absolute;left:90px;top:43px;width:198px;text-align:right;font-size:10.5px;line-height:13px;letter-spacing:.3px}
  .footer-dot{position:absolute;left:302px;top:36px;width:40px;height:40px;border-radius:50%;background:var(--white)}
  .offices{position:absolute;left:362px;top:29px;font-size:13.4px;line-height:18px}
  .offices b{font-weight:700}
</style>
</head>
<body>
<div class="document">

  <header class="header">
    <div class="header-panel"></div>
    <svg class="corner-shapes" width="120" height="80" viewBox="0 0 120 80" aria-hidden="true">
      <polygon points="20,0 120,0 120,80" fill="var(--brand-blue)"/>
      <polygon points="55,0 120,0 120,52" fill="var(--white)"/>
      <polygon points="72,0 120,0 120,38" fill="var(--brand-blue)"/>
    </svg>
    <div class="brand">
      <div class="brand-dot"></div>
      <div class="brand-name">Northline Climate<br>Supply, Inc.</div>
    </div>
    <div class="project">
      <div class="label">PROJECT ADDRESS:</div>
      <div class="project-address">Maple Ridge Care Center<br>1180 Harbor View Lane, Canton, OH, 44718</div>
    </div>
    <div class="quote-number">QUOTE: <span>Q000039</span></div>
    <div class="doc-title">QUOTATION</div>
  </header>

  <main class="terms">
    <p>STANDARD TERMS AND CONDITIONS</p>
    <p>The acceptance of any order by Northline Climate Supply, Inc. (NCS) from the buyer referenced on the face hereof or attached hereto (the Buyer), and/or Buyer's acceptance of the equipment and merchandise referenced on the face hereof or attached hereto (the Equipment) constitutes Buyer's acceptance of all of terms and conditions contained herein. Any inconsistent or additional terms contained in the Buyer's purchase order are hereby rejected. The terms and conditions as stated herein shall not be modified other than in writing signed by NCS and Buyer.</p>
    <p>All prices for the Equipment are subject to change without notice. Equipment will be billed at the prices in system at time of shipment and are F.O.B. original shipping point. Prices do not include applicable federal, state, and/or local taxes. Minimum order size is $25.</p>
    <p>2. Terms:</p>
    <p>The obligation of NCS to fulfill any Buyer order in accordance with these terms and conditions is conditioned upon Buyer paying in full the purchase price for all Equipment related to the order. Unless otherwise agreed to by NCS, payment of the full purchase price for the Equipment, plus taxes and freight where applicable, shall be due net thirty (30) days from the date of invoice (the "Payment Term") with a service charge of one and one-half percent (1½%) of the invoiced amount applying to the unpaid balance for each month, or fraction thereof, for invoices not paid in full after thirty days. A three percent (3%) service charge will be added to any payments made by credit card on balances beyond the Payment Term. Past due accounts could be placed on hold, could have intent to lien letters sent, or liens filed at NCS's discretion. If, in the sole discretion of NCS, Buyer's credit is impaired at anytime, NCS shall have the right, without incurring any liability, to change the terms of payment, stop shipment, and/or cancel any order.</p>
    <p>3. Title and Risk of Loss:</p>
    <p>Title in and risk of loss for all Equipment sold hereunder shall pass to Buyer upon delivery to carrier F.O.B. NCS's facility or NCS's supplier, as applicable.</p>
    <p>4. Cancellation. Return. Change Orders, Delivery:</p>
    <p>NCS is entitled to rely upon the receipt of either a written purchase order or email acknowledgement from Buyer in sufficient detail to enable it to fulfill any order. No orders may be withdrawn, canceled or returned by Buyer, nor may they be deferred when ready, unless NCS shall have approved such withdrawal, cancellation, return or deferral in writing and NCS shall have been paid a withdrawal, cancellation, return or deferral charge of a reasonable amount acceptable to NCS. In the event Buyer shall request changes in its order after receipt thereof by NCS, it shall be responsible for all charges reasonably incurred by NCS with respect to such changes. Only NCS stock Equipment inventory will be considered for return. No special order items may be returned under any circumstances. In the event NCS agrees to a return of stock Equipment inventory, all such Equipment shall be returned within thirty (30) days of delivery in new condition and in its original packaging and containers. All accepted returns are subject to a twenty-five percent (25%) restocking and/or handling fee. All accepted returns must include a copy of the original sales order, and a complete return goods authorization form. Any dates or schedules which may be specified for the delivery of the Equipment have been stated only approximately and are estimated from the date of release of Buyer's order, with complete specifications, designs, samples and other information reasonably requested by NCS. NCS shall not incur any liability, either direct or indirect, nor shall any order be canceled, because or as a result of any delays in meeting such dates or schedules. NCS shall not be responsible or liable for any delays or failures in manufacture or delivery due to any cause or condition beyond the control of NCS including, without limitation, strikes or labor difficulties, fire, floods, inability to secure transportation facilities, actions of the elements, shortage of materials or equipment, riots or other civil commotions, acts of God and war. NCS is not responsible for any delays caused by third party suppliers of NCS or the inability of any such third parties to deliver their goods. It is understood by Buyer that NCS's quote may be based on a quote from a third party and NCS shall not be bound by its own quote if any third party fails to provide its goods or services as agreed.</p>
    <p>5. Limited Warranty:</p>
    <p>NCS makes no warranty whatsoever, except as to title, with respect to the Equipment. All Equipment is sold with the understanding that Buyer has independently determined the suitability or compatibility of such Equipment for its purposes. Any statements, technical information or recommendations concerning Equipment sold by NCS are based upon data provided to NCS by its suppliers and believed to be accurate, but do not constitute a guarantee or warranty. Buyer's sole remedy for damaged or defective Equipment shall be through any warranty provided by the manufacturer of the Equipment (which will be made available upon request) and/or a claim against the shipper. All cartons/Equipment must be inspected and any damage claim must be reported within forty-eight (48) hours of delivery. NCS will use commercially reasonable efforts to assist Buyer in pursuing warranty claims with the manufacturer of the Equipment and resolving any claim for damages and/or losses in transit with the shipper.</p>
    <p>EXCEPT FOR THE EXPRESS WARRANTY AS DESCRIBED, THERE ARE NO OTHER WARRANTIES OR GUARANTEES, EITHER EXPRESS OR IMPLIED, WRITTEN, ORAL OR ARISING UNDER CUSTOM OF TRADE INCLUDING, WITHOUT LIMITATION, THE WARRANTIES OF MERCHANTABILITY AND FITNESS FOR ANY PARTICULAR PURPOSE. NO WARRANTIES OR REPRESENTATIONS AT ANY TIME MADE BY ANY REPRESENTATIVE OF NCS SHALL BE EFFECTIVE TO VARY OR EXPAND THE EXPRESS WARRANTY OR ANY TERMS HEREOF.</p>
    <p>6. Limitation of Liability:</p>
    <p>In no event shall NCS be liable to Buyer or to any third party for consequential, incidental or special damages, or for lost profits, resulting from or in any manner related to the Equipment, its delivery, non-delivery, design, use, or any inability to use the same, whether such damages be claimed under contract, tort or any other legal theory. Buyer understands that the sole and exclusive remedies of Buyer are those set forth in Section 5 hereof NCS's liability hereunder shall not exceed the purchase price of the Equipment that fails to meet NCS's warranty of title. This limitation of liability shall survive the termination, expiration or cancellation of these terms and conditions.</p>
    <p>7. Indemnification:</p>
    <p>Buyer shall indemnify, defend and hold harmless NCS against all claims, loss, liability and expense (including, without limitation, reasonable attorneys' fees) on account of: (A) any damaged property or injury or death of persons (including, without limitation, Buyer's employees) arising out of Buyer's unloading, storage, handling, use or disposal of the Equipment, or (B) Buyer's breach of these terms and conditions. This indemnity obligation of Buyer will survive the expiration, termination or cancellation of these terms and conditions.</p>
    <p>8. General:</p>
    <p>A. Repairs to Equipment may be done by NCS as mutually agreed by the parties. All repairs made by NCS are on an F.O.B original</p>
  </main>

  <footer class="footer">
    <svg class="footer-shapes" width="140" height="107" viewBox="0 0 140 107" aria-hidden="true">
      <polygon points="0,0 0,107 120,107" fill="var(--mid-blue)"/>
      <polygon points="0,40 0,107 70,107" fill="var(--white)"/>
      <polygon points="0,62 0,107 44,107" fill="var(--brand-blue)"/>
    </svg>
    <div class="tagline">PARTNERING WITH YOU<br>DELIVERING SOLUTIONS AND SERVICE</div>
    <div class="footer-dot"></div>
    <div class="offices">
      <div><b>CLEVELAND:</b> 2100 Ridgeline Drive, Broadview Heights, OH 44147 - <b>440.555.0134</b></div>
      <div><b>COLUMBUS:</b> 745 Market Street, Columbus, OH 43215 - <b>614.555.0172</b></div>
      <div><b>TOLEDO:</b> 4420 Orchard Road, Perrysburg, OH 43551 - <b>419.555.0188</b></div>
    </div>
  </footer>

</div>
</body>
</html>
```